Tarnabee Wines - web page for new Australian wine label

We need a landing page for our wine company. Tarnabee is a family owned company, we grow the gapes, and make the wine in the Clare valley. Daniel Hovsted is the winemaker and is well known for his style, which is all about the fruit flavour rather than wood or age influences. Tarnabee is Abriginal for 2 hills and a water source. We hand pick, hand plunge, foot crush resulting in elegant wine. Little to no additives, minimal filtering, single vineyard wines. Handcrafted with small releases of only the best fruit from carefully selected rows and bunches. The Clare valley is located two hours North of Adelaide, is known for cool climate and slow ripening, resulting in wines that have an elegant mouth feel, with bright colour and outstanding flavours. Our Sevenhill vineyard has a Eastern aspect, gathering morning sun and escaping the hot afternoons, and in our opinion is on of the prettiest valleys in the world. Only 1000 cases per annum of the very best handpicked fruit, from the best rows. We hope you enjoy the Tarnabee style, the reds are lighter in colour, fruit driven palate, more old world influence and the Riesling is on the dry side with fresh citrus. Minimal additives and filtering, our aim was to make wine with minimal influence from wine making. Handcrafted wines.

Target Market(s)

females 18 - 60 are the ones that buy 70 percent of wine, so whilst men are also a target, its the ladies we seek to appeal to.

Industry/Entity Type

It Company

Number of Pages Required

4 page

Font styles to use
Serif

Requirements
Must have
• Eye catching front page that makes me feel like i am ordering from quality company, that cares for what they do. Easy to use ordering, and delivery instructions.
• postage is $14.90 per case Australia wide.
• www.tarnabeewines.com
Nice to have
• I want to see a fun and family oriented business that cares for the wine, we dont make a lot, its buckets and feet. But its wine made wanting to be the best in the world, we dont cut corners on quality. Handcrafted
Should not have
• dont really have any thoughts here, looking for all ideas

```html
<!DOCTYPE html>
<html lang="en">
<head>
<meta charset="utf-8">
<title>Tarnabee Wines</title>
<link rel="stylesheet" href="https://fonts.googleapis.com/css2?family=Roboto:wght@300;400&family=Tinos&family=Lobster+Two:ital@1&display=swap">
<style>
:root{
  --ink:#000;
  --pink:#c982b2;
  --pink-btn:#cf8bb8;
  --text:#555;
  --grey-band:#efefef;
  --footer:#474247;
  --footer-text:#8b8489;
  --footer-line:#6a646a;
  --white:#fff;
  --glass-black:#0c0c0c;
  --label-cream:#e8e1bf;
  --capsule-blue:#2f6b93;
}
*{margin:0;padding:0;box-sizing:border-box}
html,body{width:1200px;height:2206px;overflow:hidden}
body{position:relative;font-family:'Roboto',Arial,sans-serif;background:var(--white);color:var(--text)}
h1,h2,h3{font-weight:400}
.abs{position:absolute}

/* hero */
.hero{left:0;top:0;width:1200px;height:644px;background:
  radial-gradient(ellipse at 68% 60%,#4a4a4a 0%,#262626 35%,#0d0d0d 70%),#000}
.hero-scene{left:470px;top:60px;width:590px;height:584px;background:
  radial-gradient(ellipse at 40% 75%,#2b1f33 0%,rgba(30,20,35,.6) 35%,rgba(0,0,0,0) 65%)}
.brand{left:162px;top:22px;font-family:'Tinos',serif;font-size:30px;color:var(--pink);letter-spacing:1px}
.nav{right:249px;top:31px;display:flex;gap:26px;font-size:10.5px;line-height:14px;color:var(--white);text-transform:uppercase}
.nav .active{color:var(--pink)}
.nav-sep{left:968px;top:27px;width:1px;height:20px;background:#888}
.social-dots{left:986px;top:34px;display:flex;gap:15px}
.social-dots span{width:9px;height:9px;border-radius:50%;background:var(--white)}
.slide-arrow{top:306px;width:38px;height:38px;border:1.5px solid var(--white)}
.slide-arrow svg{display:block;margin:11px auto 0}
.hero-title{left:188px;top:244px;font-family:'Lobster Two',cursive;font-style:italic;font-size:25px;line-height:33px;color:var(--white)}
.hero-title .accent{color:var(--pink);font-size:33px}
.hero-btn{left:193px;top:372px;width:113px;height:40px;border-top:1px solid var(--pink);border-bottom:1px solid var(--pink);color:#ddd;font-size:12.5px;text-align:center;line-height:38px;letter-spacing:.3px}

/* about */
.about-frame{left:222px;top:691px;width:209px;height:280px;border:4px solid #cfcfcf}
.about-photo{left:240px;top:707px;width:210px;height:281px;background:linear-gradient(160deg,#8a6a4c,#4a382b 55%,#2a2420)}
.about-label{left:512px;top:709px;font-size:14px;color:var(--pink)}
.about-heading{left:512px;top:727px;font-size:23px;font-weight:300;color:#333}
.about-body{left:512px;top:769px;width:525px;font-size:11.3px;line-height:20.2px;color:var(--text)}

/* products */
.products{left:0;top:1031px;width:1200px;height:537px;background:var(--grey-band)}
.bottle-one{left:0;top:1078px;width:612px;height:173px;background:
  linear-gradient(180deg,rgba(255,255,255,.08),rgba(0,0,0,0) 30%,rgba(0,0,0,.25)),
  linear-gradient(90deg,var(--glass-black) 0,var(--glass-black) 80px,var(--label-cream) 96px,var(--label-cream) 294px,var(--glass-black) 310px,#1c1c1c 460px,var(--capsule-blue) 490px,var(--capsule-blue) 612px)}
.bottle-two{left:592px;top:1347px;width:608px;height:173px;background:
  linear-gradient(180deg,rgba(255,255,255,.08),rgba(0,0,0,0) 30%,rgba(0,0,0,.25)),
  linear-gradient(270deg,var(--glass-black) 0,var(--glass-black) 92px,var(--label-cream) 108px,var(--label-cream) 300px,var(--glass-black) 316px,#1c1c1c 460px,var(--capsule-blue) 490px,var(--capsule-blue) 608px)}
.product-title{font-family:'Tinos',serif;font-size:18px;line-height:27px;color:var(--pink);text-transform:uppercase;letter-spacing:.4px}
.product-body{font-size:10.6px;line-height:20px;color:var(--text)}
.btn{height:37px;width:106px;background:var(--pink-btn);color:var(--white);font-size:10.5px;text-align:center;line-height:37px;text-transform:uppercase}

/* newsletter */
.news-title{left:0;top:1614px;width:1200px;text-align:center;font-family:'Tinos',serif;font-size:18px;color:var(--pink);letter-spacing:.4px}
.news-text{left:0;top:1655px;width:1200px;text-align:center;font-size:10.6px;line-height:20px;color:var(--text)}
.news-form{left:347px;top:1731px;width:506px;height:53px;border:1px solid #e3e3e3}
.news-input{left:12px;top:0;line-height:51px;font-size:10px;color:#c8c8c8;text-transform:uppercase}
.news-divider{left:401px;top:10px;width:1px;height:31px;background:#e3e3e3}
.news-submit{left:402px;width:102px;top:0;line-height:51px;text-align:center;font-size:10px;color:var(--pink);text-transform:uppercase}

/* footer */
.footer{left:0;top:1832px;width:1200px;height:374px;background:var(--footer)}
.footer-brand{left:0;top:1860px;width:1200px;text-align:center;font-family:'Tinos',serif;font-size:44px;color:#9b9499;letter-spacing:2px}
.footer-tag{left:0;top:1933px;width:1200px;text-align:center;font-family:'Tinos',serif;font-size:17px;color:#9b9499;letter-spacing:.5px}
.footer-text{left:300px;top:1967px;width:600px;text-align:center;font-size:10.5px;line-height:20px;color:var(--footer-text)}
.footer-social{top:2058px;width:33px;height:33px;border:1.5px solid #8b8489;border-radius:50%}
.footer-line{left:162px;top:2130px;width:876px;height:1px;background:var(--footer-line)}
.copyright{left:0;top:2159px;width:1200px;text-align:center;font-size:10.5px;color:var(--footer-text)}
</style>
</head>
<body>

<section class="abs hero" role="img" aria-label="Black and white vineyard path at dusk"></section>
<div class="abs hero-scene" role="img" aria-label="Bottle of red wine with a filled glass and a bunch of dark grapes"></div>
<div class="abs brand">Tarnabee</div>
<nav class="abs nav"><span class="active">Home</span><span>About</span><span>Product</span><span>Services</span><span>Contact</span></nav>
<div class="abs nav-sep"></div>
<div class="abs social-dots" aria-label="Social links"><span></span><span></span><span></span></div>
<div class="abs slide-arrow" style="left:28px" aria-label="Previous slide"><svg width="10" height="14" viewBox="0 0 10 14"><path d="M8 1 2 7l6 6" fill="none" stroke="#fff" stroke-width="2"/></svg></div>
<div class="abs slide-arrow" style="left:1136px" aria-label="Next slide"><svg width="10" height="14" viewBox="0 0 10 14"><path d="M2 1l6 6-6 6" fill="none" stroke="#fff" stroke-width="2"/></svg></div>
<h1 class="abs hero-title"><span class="accent">hand crafted</span> premium wine...<br>minimal filtering, single<br>vineyard wines</h1>
<div class="abs hero-btn">READ MORE</div>

<div class="abs about-frame"></div>
<div class="abs about-photo" role="img" aria-label="Two winemakers standing among oak barrels in the cellar"></div>
<div class="abs about-label">Message from Tarnabee</div>
<h2 class="abs about-heading">Handcrafted with small releases of only</h2>
<p class="abs about-body">Tarnabee is a family owned company, we grow the gapes, and make the wine in the Clare valley. Daniel Hovsted is the winemaker and is well known for his style, which is all about the fruit flavour rather than wood or age influences. Tarnabee is Abriginal for 2 hills and a water source. We hand pick, hand plunge, foot crush resulting in elegant wine. Little to no additives, minimal filtering, single vineyard wines. Handcrafted with small releases of only the best fruit from carefully selected rows and bunches. The Clare valley is located two hours North of Adelaide, is known for cool climate and slow ripening, resulting in wines that have an elegant mouth feel, with bright colour and outstanding flavours. Our Sevenhill vineyard has a Eastern aspect, gathering morning sun and escaping the hot afternoons, and in our opinion is on of the prettiest valleys in the world. Only 1000 cases per annum of the very best handpicked fruit, from the best rows.</p>

<section class="abs products"></section>
<div class="abs bottle-one" role="img" aria-label="Bottle of 2016 Reserve Shiraz lying on its side, cream label and blue capsule"></div>
<h3 class="abs product-title" style="left:669px;top:1087px">2016 Reserve Shiraz Single Vineyard<br>Sevenhill Clare Valley</h3>
<p class="abs product-body" style="left:669px;top:1157px;width:375px">Lorem ipsum dolor sit amet, consectetur adipiscing elit. Pellentesque volutpat eget nibh eu laoreet. Nulla efficitur leo consectetur, mollis lorem vel, vehicula orci. Ut euismod vitae erat id tempor.</p>
<div class="abs btn" style="left:669px;top:1241px">Read more</div>

<h3 class="abs product-title" style="left:168px;top:1297px">2016 Shiraz<br>Clare Valley</h3>
<p class="abs product-body" style="left:168px;top:1366px;width:375px">Lorem ipsum dolor sit amet, consectetur adipiscing elit. Pellentesque volutpat eget nibh eu laoreet. Nulla efficitur leo consectetur, mollis lorem vel, vehicula orci. Ut euismod vitae erat id tempor.</p>
<div class="abs btn" style="left:168px;top:1450px">Read more</div>
<div class="abs bottle-two" role="img" aria-label="Bottle of 2016 Shiraz lying on its side, cream label and blue capsule"></div>

<h3 class="abs news-title">JOIN OUR NEWSLETTER</h3>
<p class="abs news-text">Lorem ipsum dolor sit amet, consectetur adipiscing elit.<br>Proin blandit vitae quam id pellentesque.</p>
<div class="abs news-form">
  <span class="abs news-input">Email address</span>
  <span class="abs news-divider"></span>
  <span class="abs news-submit">Sign up</span>
</div>

<footer class="abs footer"></footer>
<div class="abs footer-brand">Tarnabee</div>
<div class="abs footer-tag">WE MAKE GOOD WINES.</div>
<p class="abs footer-text">Proin fringilla faucibus eleifend. Donec ultricies elit eget cursus consequat. Nunc nec congue ligula. Mauris et elit risus. Fusce placerat blandit neque. Fusce facilisis, augue malesuada luctus consectetur, magna leo tempor metus, et dignissim purus lorem rhoncus enim. Ut ac magna et leo tristique porttitor. Nullam lobortis nisl at cursus pharetra.</p>
<span class="abs footer-social" style="left:532px" aria-label="Social link"></span>
<span class="abs footer-social" style="left:583px" aria-label="Social link"></span>
<span class="abs footer-social" style="left:632px" aria-label="Social link"></span>
<div class="abs footer-line"></div>
<div class="abs copyright">© 2017 Tarnabee. All rights reserved</div>

</body>
</html>
```